Agency needs 2 x EDM executions

We’re Brindle, a word of mouth marketing agency. We have a community of people who participate in projects that range from being sent free products to trying new services to road test. Pretty fun stuff!

We’re looking for a designer to create two EDM (electronic direct marketing) executions. These EDMs will be used as an email to get people to join and become a Brindle member.

Previous examples of our EDMs are attached, but we’re looking for some fresh new design ideas! Look & feel to be fun, playful, easy on the eye. Most of all they need to be attention grabbing and motivating enough for the readers to click through and join (rather than scanning and deleting the email!).

The two executions we require will differ slightly in content and design. Copy that needs to be included in each of the EDMs is attached.

Specifically, version 1:
• Needs to include two event photos with their description below, similar to Clipwall (refer to copy document as a guide)
• Include a collage of recent product images (again, can see a guide in the copy document). Due to space restrictions you may only be able to fit one or two lines of a collage.
• Down the bottom is a quote from a member, we would like to see this stand out from the rest of the text.

And version 2:
• This will also have a collage of recent product images, but because this version has more space you can fit more images.
• This time there are two quotes from two different members.

The EDMs need to be:
• 550 pixels wide and 1000 pixels in height.
• JPEG

Please visit our website to get an idea of our branding: www.thebrindle.com.au

Requirements
Must have
• Both designs need to include:

• Copy which is found in the attached document
• Brindle logo
• ‘Join now’ button (call to action)
• Website URL: thebrindle.com.au
• Century gothic font and luna font.
Nice to have
• Whilst the background doesn’t need to be all yellow, and can be white, we’d like to have at least some yellow per branding. The yellow we use is 100% yellow.

```html
<!DOCTYPE html>
<html lang="en">
<head>
<meta charset="utf-8">
<title>Brindle EDM – Option 02 Version 02</title>
<link href="https://fonts.googleapis.com/css2?family=Gochi+Hand&family=Didact+Gothic&family=Arimo:wght@700&display=swap" rel="stylesheet">
<style>
  :root {
    --stage: #000000;
    --paper: #ffffff;
    --yellow: #fff200;
    --ink: #1a1a1a;
    --muted: #444444;
    --label: #ffffff;
  }
  * { margin: 0; padding: 0; box-sizing: border-box; }
  html, body { width: 1200px; height: 900px; overflow: hidden; background: var(--stage); }
  .stage { position: relative; width: 1200px; height: 900px; }
  .option-label {
    position: absolute; left: 50px; top: 78px;
    font-family: "Arimo", Arial, sans-serif; font-weight: 700;
    font-size: 27px; line-height: 42px; color: var(--label);
  }
  .edm {
    position: absolute; left: 370px; top: 20px; width: 460px; height: 854px;
    background: var(--paper); color: var(--ink);
    font-family: "Didact Gothic", "Century Gothic", sans-serif;
  }
  .headline {
    position: absolute; left: 28px; right: 28px; top: 22px;
    font-family: "Gochi Hand", cursive; font-weight: 400; font-size: 23px; line-height: 28px;
    text-align: center; color: var(--ink);
  }
  .band { position: absolute; left: 0; right: 0; background: var(--yellow); }
  .band-steps { top: 150px; height: 34px; }
  .band-steps h2 {
    font-family: "Gochi Hand", cursive; font-weight: 400; font-size: 27px;
    line-height: 34px; padding-left: 28px;
  }
  .steps {
    position: absolute; left: 28px; right: 56px; top: 202px; list-style: none;
    font-size: 12px; line-height: 15px;
  }
  .steps li { position: relative; padding-left: 20px; margin-bottom: 10px; }
  .steps li::before {
    content: ""; position: absolute; left: 2px; top: 3px; width: 8px; height: 8px;
    border: 2px solid #9c9a1a; border-radius: 50%; background: var(--yellow);
  }
  .band-products { top: 396px; height: 64px; }
  .band-products h2 {
    font-weight: 400; font-size: 17px; line-height: 21px; padding: 10px 0 0 30px; width: 300px;
  }
  .join-button {
    position: absolute; left: 336px; top: 392px; width: 72px; height: 72px;
    border-radius: 50%; background: var(--yellow); border: 4px solid var(--paper);
    box-shadow: 0 0 0 2px #d8cf00;
    display: flex; align-items: center; justify-content: center; text-align: center;
    font-family: "Arimo", Arial, sans-serif; font-weight: 700; font-size: 18px; line-height: 19px;
    color: var(--ink); text-decoration: none;
  }
  .collage { position: absolute; }
  .collage-top { left: 16px; right: 16px; top: 472px; height: 66px;
    background: linear-gradient(90deg, #d9e8ef, #f2d23a 30%, #3aa0d8 50%, #e7e2d2 70%, #b23a2a); }
  .collage-bottom { left: 66px; right: 62px; top: 544px; height: 60px;
    background: linear-gradient(90deg, #a8322a, #5aa040 35%, #2a2a2a 60%, #3fa7a0 85%, #d8d8d8); }
  .quote {
    position: absolute; left: 52px; right: 32px; font-size: 11.5px; line-height: 15px;
    color: var(--muted);
  }
  .quote::before {
    content: "\201C"; position: absolute; left: -22px; top: -6px;
    font-family: Georgia, serif; font-size: 40px; line-height: 40px; color: var(--ink); font-weight: 700;
  }
  .quote cite { font-style: normal; font-size: 7px; margin-left: 4px; }
  .quote-one { top: 620px; }
  .quote-two { top: 682px; }
  .brand {
    position: absolute; left: 0; right: 0; top: 764px; text-align: center;
    font-family: "Didact Gothic", "Century Gothic", sans-serif; font-weight: 400;
    font-size: 32px; line-height: 36px; color: var(--ink);
  }
  .band-footer { top: 836px; height: 18px; text-align: center; }
  .band-footer a {
    font-family: "Arimo", Arial, sans-serif; font-weight: 700; font-size: 10px; line-height: 18px;
    color: var(--ink); text-decoration: none;
  }
</style>
</head>
<body>
<div class="stage">
  <div class="option-label">Option: 02<br>Version: 02</div>

  <main class="edm">
    <h1 class="headline">Join Brindle and trial the latest products<br>in exchange for your honest opinion and<br>sharing with friends!</h1>

    <div class="band band-steps"><h2>It works like this:</h2></div>
    <ul class="steps">
      <li>Join Brindle by answering a few simple questions about yourself.</li>
      <li>We contact you when we have a project matching your interests.</li>
      <li>You opt in (or out) if you want to be involved.</li>
      <li>You try, share and talk about the product or service (which we'll send to you for free!)</li>
      <li>Tell us your honest opinion on what you and your friends thought.</li>
      <li>We'll share the results of each project – so you'll know the impact of all of your opinions.</li>
    </ul>

    <div class="band band-products"><h2>Products Brindle members recently trialled include:</h2></div>
    <a class="join-button" href="#">Join<br>us</a>

    <div class="collage collage-top" role="img" aria-label="Collage of recently trialled products: snacks, pantry items, personal care and drinks"></div>
    <div class="collage collage-bottom" role="img" aria-label="Second row of trialled products: wines, bottled drinks and packaged goods"></div>

    <p class="quote quote-one">It was such a fun project. I had a great time sharing it around and loved being the one to introduce such a great product to my friends! <cite>Maree, NSW</cite></p>
    <p class="quote quote-two">I loved it. It gave me a good reason to get people I like to be with together and enjoy a unique experience. I was all round a lot of fun! <cite>Dylan, QLD</cite></p>

    <div class="brand">brindle</div>

    <div class="band band-footer"><a href="#">www.thebrindle.com.au</a></div>
  </main>
</div>
</body>
</html>
```